Harwick Legal

To update and modernize current business card appearance. Marta's business is based in Melbourne with 4 other lawyers in the firm. Marta travels to the Pilbara in Western Australia approximately 1 week a month as part of the firms legal work. She consults with clients in Newman, Tom Price and Port Hedland. The lawyers work mostly from a home office, apart from court appearances. They have a virtual office in Melbourne city, and use facilities in 3 or 4 other locations around Melbourne. It is important the client's think this is a conventional law firm with a permanent office. Our business structure is a difficult concept for them to grasp. The business has been operational for 3 years, growing from 1 lawyer to 4 lawyers during that time. Our website is www.Harwicklegal.example.au and is currently being upgraded as we are not happy with its content. The logo is currently orange and dark grey but the orange is a difficult colour to reproduce and often turns out "poo" brown when documents are printed. We need clients to know we are user friendly and caring - and not head up our rears ends as some lawyers appear to be.
Updates

Thank you for the feedback so far. 1. Some of the designs have too much black (We prefer darker grey & not too much.) 2. Happy for designers to play around with different colours & logo design. What we're after is a modern look and business card that people say "wow" when they pick it up.

Industry/Entity Type

Business

```html
<!DOCTYPE html>
<html lang="en">
<head>
<meta charset="utf-8">
<title>Harwick Legal — Business Card</title>
<link rel="stylesheet" href="https://fonts.googleapis.com/css2?family=Cinzel:wght@400;500&family=Open+Sans:wght@400;600&display=swap">
<style>
  :root {
    --backdrop: #8a5d3b;
    --charcoal: #545050;
    --ink: #5a5656;
    --coral: #ee654b;
    --silver: #c9c9c9;
    --paper: #ffffff;
    --paper-shade: #f1f1f1;
  }
  * { margin: 0; padding: 0; box-sizing: border-box; }
  html, body {
    width: 1200px;
    height: 480px;
    overflow: hidden;
    background: var(--backdrop);
  }
  .stage { position: relative; width: 1200px; height: 480px; }

  .card {
    position: absolute;
    width: 475px;
    height: 270px;
    overflow: hidden;
    background: linear-gradient(100deg, var(--paper) 0%, var(--paper-shade) 45%, var(--paper) 100%);
  }
  .card--front { left: 85px; top: 93px; }
  .card--back  { left: 593px; top: 93px; }

  .card__waves { position: absolute; inset: 0; width: 475px; height: 270px; }

  .brand {
    position: absolute;
    display: flex;
    flex-direction: column;
    align-items: center;
  }
  .brand__dot {
    width: 34px;
    height: 34px;
    border-radius: 50%;
    background: var(--coral);
    margin-bottom: 12px;
  }
  .brand__name {
    font-family: "Cinzel", serif;
    font-weight: 500;
    color: var(--ink);
    white-space: nowrap;
    letter-spacing: 0.5px;
  }
  .card--front .brand { left: 40px; top: 102px; width: 190px; }
  .card--front .brand__name { font-size: 21px; }
  .card--back .brand { left: 0; top: 76px; width: 475px; }
  .card--back .brand__dot { width: 44px; height: 44px; margin-bottom: 16px; }
  .card--back .brand__name { font-size: 28px; }

  .contact {
    position: absolute;
    right: 28px;
    top: 77px;
    text-align: right;
    font-family: "Open Sans", sans-serif;
    color: var(--ink);
    font-size: 11px;
    line-height: 1;
  }
  .contact__line { font-weight: 600; margin-bottom: 9px; letter-spacing: 0.2px; }
  .contact__address { font-weight: 400; font-size: 10px; line-height: 14px; margin-top: 5px; }

  .holder-name {
    position: absolute;
    right: 28px;
    top: 219px;
    font-family: "Cinzel", serif;
    font-weight: 400;
    font-size: 17px;
    color: var(--paper);
    letter-spacing: 0.6px;
  }

  .web {
    position: absolute;
    left: 0;
    top: 209px;
    width: 475px;
    text-align: center;
    font-family: "Open Sans", sans-serif;
    font-weight: 600;
    font-size: 12px;
    letter-spacing: 0.8px;
    color: var(--ink);
  }
</style>
</head>
<body>
<main class="stage">

  <section class="card card--front" aria-label="Business card front">
    <svg class="card__waves" viewBox="0 0 475 270" aria-hidden="true">
      <!-- top band -->
      <path fill="var(--silver)" opacity="0.6" d="M0,0 H475 V55 C440,44 400,36 330,42 C230,52 120,106 0,82 Z"/>
      <path fill="var(--coral)" d="M0,0 H475 V47 C440,36 400,28 330,34 C230,44 120,98 0,74 Z"/>
      <path fill="var(--charcoal)" d="M0,0 H475 V38 C440,28 400,20 330,26 C230,36 120,90 0,66 Z"/>
      <!-- bottom band -->
      <path fill="var(--coral)" d="M0,196 C100,240 220,250 300,224 C380,198 430,180 475,176 V270 H0 Z"/>
      <path fill="var(--silver)" d="M0,206 C100,250 220,258 300,232 C380,206 430,188 475,184 V270 H0 Z"/>
      <path fill="var(--charcoal)" d="M0,211 C100,255 220,263 300,237 C380,211 430,193 475,189 V270 H0 Z"/>
    </svg>

    <div class="brand">
      <span class="brand__dot"></span>
      <span class="brand__name">Harwick Legal</span>
    </div>

    <address class="contact" style="font-style:normal">
      <p class="contact__line">Tel: 012.555.0189</p>
      <p class="contact__line">Email: info@harwick.example</p>
      <p class="contact__line">www.Harwicklegal.example.au</p>
      <p class="contact__address">Suite 000, Cityname<br>country name</p>
    </address>

    <p class="holder-name">Your name here</p>
  </section>

  <section class="card card--back" aria-label="Business card back">
    <div class="brand">
      <span class="brand__dot"></span>
      <span class="brand__name">Harwick Legal</span>
    </div>
    <p class="web">www.Harwicklegal.example.au</p>
  </section>

</main>
</body>
</html>
```